Facebook Header Design Project.

I'm supplying white and colored logos. The Facebook page already exists. URL = https://www.examplesocial.test/lumacrest.design The design should not be based on what's already there. Consider mobile implications of the design. This Design will form the designs of other social media headers. LumaCrest is a web design | digital marketing company.

Target Market(s)

People interested in web design | digital marketing services.

Industry/Entity Type

LumaCrest is a web design | digital marketing company. That should be clear in the design.

Colors
0054AA
0677BA
7BADD7
CADEEF
E8F1F8

Requirements
Must have
• Logo. Use Facebook header image dimension.
Nice to have
• Use a color scheme like the logo and feel free to add a color or two from the other side of the color whee.

```html
<!DOCTYPE html>
<html lang="en">
<head>
<meta charset="utf-8">
<title>LumaCrest – Social Header</title>
<link rel="stylesheet" href="https://fonts.googleapis.com/css2?family=Raleway:wght@300;400;700;800&display=swap">
<style>
  :root {
    --page-bg: #ffffff;
    --cover-blue: #2358a4;
    --cover-blue-light: #2a6cbf;
    --accent-blue: #0677ba;
    --circle-blue: #137ac4;
    --pale-blue: #cadeef;
    --text-blue: #1f5aa6;
    --white: #ffffff;
  }
  html, body {
    margin: 0;
    width: 1200px;
    height: 1200px;
    overflow: hidden;
    background: var(--page-bg);
  }
  .canvas {
    position: relative;
    width: 1200px;
    height: 1200px;
  }
  .cover {
    position: absolute;
    left: 40px;
    top: 354px;
    width: 1120px;
    height: 491px;
    display: block;
  }
  .brand-name {
    font-family: "Raleway", sans-serif;
    font-weight: 800;
    font-size: 74px;
    fill: var(--white);
    letter-spacing: 1px;
  }
  .tagline {
    font-family: "Raleway", sans-serif;
    fill: var(--white);
  }
  .tagline-light { font-weight: 400; }
  .tagline-bold { font-weight: 800; }
  .tagline-highlight {
    font-family: "Raleway", sans-serif;
    font-weight: 800;
    fill: var(--text-blue);
  }
</style>
</head>
<body>
<main class="canvas">
  <svg class="cover" viewBox="0 0 1122 492" xmlns="http://www.w3.org/2000/svg">
    <defs>
      <linearGradient id="photoTone" x1="0" y1="0" x2="0" y2="1">
        <stop offset="0" stop-color="#d9b58a"/>
        <stop offset="0.45" stop-color="#eeeae6"/>
        <stop offset="1" stop-color="#5a6e8c"/>
      </linearGradient>
      <clipPath id="coverClip"><rect width="1122" height="492"/></clipPath>
    </defs>

    <g clip-path="url(#coverClip)">
      <!-- background -->
      <rect class="cover-bg" width="1122" height="492" fill="var(--cover-blue)"/>
      <path class="wave-lower" d="M0 230 C120 215 250 250 350 300 C450 350 520 420 560 492 L0 492 Z" fill="var(--cover-blue-light)"/>
      <path class="wave-right" d="M700 0 L1122 0 L1122 492 L1000 492 C1060 380 1000 250 900 170 C830 110 760 60 700 0 Z" fill="var(--cover-blue-light)"/>
      <path class="arc-line" d="M0 197 C120 180 240 110 290 0" fill="none" stroke="var(--pale-blue)" stroke-opacity="0.6" stroke-width="1.5"/>
      <path class="arc-line" d="M350 0 L388 38" fill="none" stroke="var(--pale-blue)" stroke-opacity="0.6" stroke-width="1.5"/>
      <path class="arc-line" d="M0 432 A42 42 0 0 1 42 474 L42 492" fill="none" stroke="var(--pale-blue)" stroke-opacity="0.6" stroke-width="1.5"/>
      <circle cx="483" cy="33" r="3.5" fill="var(--white)"/>

      <!-- large backdrop circle -->
      <circle class="backdrop-circle" cx="790" cy="290" r="205" fill="var(--circle-blue)"/>

      <!-- capsules -->
      <line x1="640" y1="110" x2="675" y2="78" stroke="var(--accent-blue)" stroke-width="34" stroke-linecap="round"/>
      <line x1="605" y1="430" x2="625" y2="410" stroke="var(--accent-blue)" stroke-width="30" stroke-linecap="round"/>
      <line x1="990" y1="60" x2="1010" y2="45" stroke="var(--accent-blue)" stroke-width="34" stroke-linecap="round"/>
      <line x1="1012" y1="378" x2="1030" y2="362" stroke="var(--accent-blue)" stroke-width="34" stroke-linecap="round"/>

      <!-- photo area -->
      <rect role="img" aria-label="Photo of a cheering woman in a white t-shirt holding an open laptop" x="590" y="36" width="400" height="456" rx="170" fill="url(#photoTone)"/>

      <!-- diagonal strokes -->
      <line x1="520" y1="441" x2="612" y2="352" stroke="var(--white)" stroke-width="18" stroke-linecap="round"/>
      <line x1="513" y1="423" x2="610" y2="320" stroke="var(--white)" stroke-width="1.5" stroke-linecap="round" opacity="0.8"/>
      <line x1="995" y1="140" x2="1090" y2="52" stroke="var(--white)" stroke-width="18" stroke-linecap="round"/>
      <line x1="990" y1="170" x2="1090" y2="75" stroke="var(--white)" stroke-width="1.5" stroke-linecap="round" opacity="0.8"/>

      <!-- brand name -->
      <text class="brand-name" x="362" y="232" text-anchor="middle">LumaCrest</text>

      <!-- tagline -->
      <text class="tagline" x="362" y="303" text-anchor="middle" font-size="36">
        <tspan class="tagline-light">IS A </tspan><tspan class="tagline-bold">WEB DESIGN \</tspan>
      </text>
      <path d="M163 313 L600 313 L575 352 L163 352 A19.5 19.5 0 0 1 163 313 Z" fill="var(--white)"/>
      <text class="tagline-highlight" x="360" y="346" text-anchor="middle" font-size="36">DIGITAL MARKETING</text>
      <text class="tagline tagline-light" x="360" y="382" text-anchor="middle" font-size="32">COMPANY.</text>
    </g>
  </svg>
</main>
</body>
</html>
```